Business Card for Marriage Commissioner

I am a marriage commissioner in the province of Alberta, meaning that I perform civil unions here. I have been trying to think of a unique design for my business card, something a bit different. A lot of "unique" designs seem to incorporate unique cuts or "some assembly required" or printed on plastic or meat. I would like my design to be a full colour card that is a typical business card size.

The information on the card should have:
Lon Varbeck
my occupation: Marriage Commissioner
my website: www.lonvarbeck.ca
my e-mail: lon@lonvarbeck.ca
my phone: 780-914-2086

I originally submitted a design to the printer that had a screen capture of a finduro search window, with my name and occupation in the text box. And underneath that, my phone number. Nothing else. They indicated they could not print this because it was a copyright violation.

One option on the design is I am a retired chemist-so a chemistry themed card would also be of interest, as long as it isn't a "Quiet Reagent" theme, as I have that on my other business cards already...

I would prefer a single sided card, but I am open to a double sided card if it is clever!

I would also prefer not to have pictures of male and female couples as in my position I will also marry same sex couples. Same thing for male/female symbols. Someone has submitted two graduated cylinders in love, which is very clever, and gets around this male/female type.

Thanks for your help and interest.

Target Market(s)

Young couples.

Industry/Entity Type

Plastic

Requirements
Nice to have
• chemistry ideas!
Should not have
• Male/female pictures, male/female symbols.
No QR codes.
No transparent designs, will go on paper stock.

```html
<!DOCTYPE html>
<html lang="en">
<head>
<meta charset="utf-8">
<title>Lon Varbeck – Marriage Commissioner</title>
<link rel="stylesheet" href="https://fonts.googleapis.com/css2?family=Source+Sans+3:wght@400&display=swap">
<style>
  :root {
    --navy: #020b4c;
    --navy-soft: #0a1660;
    --copper: #d18f60;
    --copper-band: #c9895e;
    --lilac: #a47ca4;
    --lilac-band: #a07598;
    --glass: #f4f4f6;
  }
  html, body {
    margin: 0;
    padding: 0;
    width: 1200px;
    height: 686px;
    overflow: hidden;
    background: var(--navy);
  }
  .card {
    position: relative;
    width: 1200px;
    height: 686px;
    background: var(--navy);
    font-family: "Source Sans 3", "Myriad Pro", Arial, sans-serif;
    overflow: hidden;
  }
  .flourish {
    position: absolute;
    left: 300px;
    top: 0;
    width: 540px;
    height: 600px;
    background: radial-gradient(ellipse 50% 45% at 52% 58%, var(--navy-soft) 0%, rgba(10,22,96,0.55) 55%, rgba(2,11,76,0) 100%);
  }
  .cylinders {
    position: absolute;
    left: 0;
    top: 28px;
    width: 262px;
    height: 566px;
    border-radius: 0 14px 14px 0;
    background: linear-gradient(180deg,
      rgba(164,124,164,0.35) 0%,
      rgba(209,143,96,0.35) 20%,
      var(--glass) 23%,
      var(--glass) 54%,
      var(--copper) 57%,
      var(--copper) 72%,
      var(--lilac) 75%,
      var(--lilac) 92%,
      var(--navy) 100%);
  }
  .name {
    position: absolute;
    left: 434px;
    top: 84px;
    margin: 0;
    font-size: 78px;
    font-weight: 400;
    line-height: 1;
    color: var(--copper);
  }
  .occupation {
    position: absolute;
    left: 356px;
    top: 175px;
    margin: 0;
    font-size: 48px;
    font-weight: 400;
    line-height: 1;
    color: var(--lilac);
  }
  .contact {
    position: absolute;
    left: 748px;
    top: 430px;
    margin: 0;
    font-size: 35px;
    line-height: 1;
  }
  .contact-row {
    display: flex;
    height: 57px;
    align-items: baseline;
  }
  .contact-label {
    width: 141px;
    color: var(--lilac);
    white-space: pre;
  }
  .contact-value {
    color: var(--copper);
  }
  .band-copper {
    position: absolute;
    left: 0;
    top: 608px;
    width: 1200px;
    height: 23px;
    background: var(--copper-band);
  }
  .band-lilac {
    position: absolute;
    left: 0;
    top: 631px;
    width: 1200px;
    height: 55px;
    background: var(--lilac-band);
  }
</style>
</head>
<body>
  <div class="card">
    <div class="flourish" role="img" aria-label="Faint embossed swirling heart ornament"></div>
    <div class="cylinders" role="img" aria-label="Illustration of two graduated cylinders leaning together in love, filled with copper and lilac liquid, with small hearts floating above"></div>

    <h1 class="name">Lon Varbeck</h1>
    <p class="occupation">Marriage Commissioner</p>

    <div class="contact">
      <div class="contact-row"><span class="contact-label">website:</span><span class="contact-value">www.lonvarbeck.ca</span></div>
      <div class="contact-row"><span class="contact-label"> e-mail  :</span><span class="contact-value">lon@lonvarbeck.ca</span></div>
      <div class="contact-row"><span class="contact-label"> phone :</span><span class="contact-value">780-914-2086</span></div>
    </div>

    <div class="band-copper"></div>
    <div class="band-lilac"></div>
  </div>
</body>
</html>
```